Upgrade UI for an existing app

I have an app that is already in the appstore, and I have finally get to the point where the app is fairly complete in its user flow and app features.

I would like to take the app to the next level, and completely revamp its look and feel, to give it that flat iOS7 look.

The app can be downloaded at https://apps.vendrulo.example/us/app/brindle-kto/id574093186?mt=8

And you can log into the app using the credential below:

sketch.harbor
password

I am also open to new ideas around UX, but my biggest focus is on getting the UI updated, especially for the setting page, support page, and about page.

Thanks,

Rob

Majority of the submissions are for iPhone, whereas I was hoping for more iPad redesign.

I think the issue is that, a lot of people didn't download the app from appstore.

I have uploaded two zip files with iPad screenshot.  Please submit a few designs that are based off the existing iPad screenshot.

```html
<!DOCTYPE html>
<html lang="en">
<head>
<meta charset="utf-8">
<title>My Exams</title>
<link rel="stylesheet" href="https://fonts.googleapis.com/css2?family=Heebo:wght@300;400&display=swap">
<style>
  :root {
    --bar-dark: #2b2e33;
    --mint: #2ec99b;
    --mint-deep: #1f9f7a;
    --ice: #e8faff;
    --white: #ffffff;
    --ink: #111111;
    --tab-active: #000000;
    --dial-core: #4d5e58;
    --dial-face: #eafaf6;
    --dial-track: #c9d3d0;
  }
  * { box-sizing: border-box; margin: 0; padding: 0; }
  html, body { width: 675px; height: 1200px; overflow: hidden; }
  body {
    font-family: "Heebo", "Helvetica Neue", Arial, sans-serif;
    background: var(--mint);
    position: relative;
    color: var(--white);
  }
  .status-bar {
    position: absolute; left: 0; top: 0; width: 675px; height: 51px;
    background: var(--bar-dark);
    font-size: 22px; font-weight: 400;
  }
  .status-bar .carrier { position: absolute; left: 12px; top: 9px; display: flex; align-items: center; gap: 6px; }
  .status-bar .signal { display: flex; gap: 3px; }
  .status-bar .signal span { width: 11px; height: 11px; border-radius: 50%; border: 1.5px solid var(--white); }
  .status-bar .signal span.on { background: var(--white); }
  .status-bar .time { position: absolute; left: 0; right: 0; top: 8px; text-align: center; }
  .status-bar .battery { position: absolute; right: 12px; top: 9px; display: flex; align-items: center; gap: 8px; }
  .battery-cell { width: 48px; height: 22px; border: 2px solid var(--white); border-radius: 4px; padding: 2px; position: relative; }
  .battery-cell::before { content: ""; display: block; width: 100%; height: 100%; background: var(--white); border-radius: 1px; }
  .battery-cell::after { content: ""; position: absolute; right: -6px; top: 5px; width: 3px; height: 8px; background: var(--white); border-radius: 0 2px 2px 0; }

  .nav-bar {
    position: absolute; left: 0; top: 51px; width: 675px; height: 95px;
    background: var(--bar-dark);
  }
  .nav-bar .menu { position: absolute; left: 13px; top: 27px; width: 46px; }
  .nav-bar .menu span { display: block; height: 5px; background: var(--white); margin-bottom: 11px; }
  .nav-bar h1 {
    position: absolute; left: 0; right: 0; top: 16px; text-align: center;
    font-weight: 300; font-size: 47px; letter-spacing: 0.5px;
  }

  .exam-summary {
    position: absolute; left: 0; top: 146px; width: 675px; height: 240px;
    background: var(--ice); color: var(--ink);
  }
  .exam-summary .status-mark { position: absolute; left: 54px; top: 50px; }
  .exam-summary h2 { position: absolute; left: 217px; top: 42px; font-weight: 400; font-size: 40px; }
  .exam-summary .size { position: absolute; left: 218px; top: 122px; font-size: 22px; }
  .exam-summary .credits { position: absolute; left: 217px; top: 153px; font-size: 22px; color: var(--mint-deep); }

  .actions {
    position: absolute; left: 0; top: 386px; width: 675px; height: 114px;
    background: var(--mint); display: flex;
  }
  .actions .action {
    flex: 1; border-right: 1px solid var(--white);
    display: flex; flex-direction: column; align-items: center;
    padding-top: 19px; font-size: 28px; font-weight: 300;
  }
  .actions .action:last-child { border-right: 0; }
  .actions .action span { margin-top: 3px; }

  .gap { position: absolute; left: 0; top: 500px; width: 675px; height: 17px; background: var(--ice); }

  .tabs {
    position: absolute; left: 0; top: 517px; width: 675px; height: 49px;
    display: flex; background: var(--mint);
  }
  .tabs .tab {
    display: flex; align-items: center; justify-content: center;
    font-size: 27px; font-weight: 300; border-right: 1px solid var(--white);
  }
  .tabs .tab:nth-child(1) { width: 225px; }
  .tabs .tab:nth-child(2) { width: 225px; }
  .tabs .tab:nth-child(3) { flex: 1; border-right: 0; background: var(--tab-active); }

  .topic-list {
    position: absolute; left: 0; top: 566px; width: 675px; list-style: none;
    border-top: 3px solid var(--white);
  }
  .topic {
    position: relative; height: 146px; border-bottom: 1px solid rgba(255,255,255,0.35);
  }
  .topic .dial { position: absolute; left: 10px; top: 22px; }
  .topic .name { position: absolute; left: 130px; top: 30px; font-size: 30px; font-weight: 300; }
  .topic .progress { position: absolute; left: 130px; top: 72px; font-size: 22px; font-weight: 300; }
  .topic .chevron { position: absolute; right: 16px; top: 48px; }
</style>
</head>
<body>
  <header class="status-bar">
    <div class="carrier">
      <div class="signal"><span class="on"></span><span class="on"></span><span class="on"></span><span></span><span></span></div>
      <span>KESTREL</span>
      <svg width="24" height="18" viewBox="0 0 24 18" aria-hidden="true">
        <path d="M2 7 A14 14 0 0 1 22 7" fill="none" stroke="#fff" stroke-width="2.5"/>
        <path d="M6 11 A8.5 8.5 0 0 1 18 11" fill="none" stroke="#fff" stroke-width="2.5"/>
        <path d="M12 17 L9 14 A4 4 0 0 1 15 14 Z" fill="#fff"/>
      </svg>
    </div>
    <div class="time">4:21 PM</div>
    <div class="battery"><span>100%</span><div class="battery-cell"></div></div>
  </header>

  <nav class="nav-bar">
    <div class="menu"><span></span><span></span><span></span></div>
    <h1>My Exams</h1>
  </nav>

  <section class="exam-summary">
    <svg class="status-mark" width="142" height="142" viewBox="0 0 142 142" aria-hidden="true">
      <circle cx="71" cy="71" r="66" fill="none" stroke="var(--mint)" stroke-width="5"/>
      <circle cx="71" cy="71" r="48" fill="var(--mint)"/>
      <path d="M47 72 L64 89 L96 56" fill="none" stroke="#fff" stroke-width="8" stroke-linecap="round" stroke-linejoin="round"/>
    </svg>
    <h2>Clinical Pathology</h2>
    <p class="size">52.49 MB</p>
    <p class="credits">12 CME/MOC</p>
  </section>

  <section class="actions">
    <div class="action"><svg width="40" height="40" viewBox="0 0 40 40" aria-hidden="true"><circle cx="20" cy="20" r="18" fill="none" stroke="#fff" stroke-width="2"/><path d="M15 11 L29 20 L15 29 Z" fill="#fff"/></svg><span>Start</span></div>
    <div class="action"><svg width="40" height="40" viewBox="0 0 40 40" aria-hidden="true"><circle cx="20" cy="20" r="18" fill="none" stroke="#fff" stroke-width="2"/><path d="M15 11 L29 20 L15 29 Z" fill="#fff"/></svg><span>Report</span></div>
    <div class="action"><svg width="40" height="40" viewBox="0 0 40 40" aria-hidden="true"><circle cx="20" cy="20" r="18" fill="none" stroke="#fff" stroke-width="2"/><path d="M15 11 L29 20 L15 29 Z" fill="#fff"/></svg><span>Reset</span></div>
    <div class="action"><svg width="40" height="40" viewBox="0 0 40 40" aria-hidden="true"><circle cx="20" cy="20" r="18" fill="none" stroke="#fff" stroke-width="2"/><path d="M15 11 L29 20 L15 29 Z" fill="#fff"/></svg><span>Submit</span></div>
  </section>

  <div class="gap"></div>

  <div class="tabs">
    <div class="tab">Details</div>
    <div class="tab">Bookmark</div>
    <div class="tab">Topics</div>
  </div>

  <ul class="topic-list">
    <li class="topic">
      <svg class="dial" width="86" height="86" viewBox="0 0 86 86" aria-hidden="true">
        <circle cx="43" cy="43" r="40" fill="var(--dial-face)" stroke="#fff" stroke-width="3"/>
        <circle cx="43" cy="43" r="35" fill="none" stroke="var(--mint)" stroke-width="2"/>
        <path d="M43 43 L43 9 A34 34 0 0 1 63 15 Z" fill="var(--dial-track)"/>
        <circle cx="43" cy="43" r="26" fill="var(--dial-core)"/>
      </svg>
      <p class="name">Ethics</p>
      <p class="progress">2 of 2 answered</p>
      <svg class="chevron" width="22" height="48" viewBox="0 0 22 48" aria-hidden="true"><path d="M2 2 L20 24 L2 46" fill="none" stroke="#fff" stroke-width="2"/></svg>
    </li>
    <li class="topic">
      <svg class="dial" width="86" height="86" viewBox="0 0 86 86" aria-hidden="true">
        <circle cx="43" cy="43" r="40" fill="var(--dial-face)" stroke="#fff" stroke-width="3"/>
        <circle cx="43" cy="43" r="35" fill="none" stroke="var(--mint)" stroke-width="2"/>
        <path d="M43 43 L43 9 A34 34 0 0 1 63 15 Z" fill="var(--dial-track)"/>
        <circle cx="43" cy="43" r="26" fill="var(--dial-core)"/>
      </svg>
      <p class="name">Ethics</p>
      <p class="progress">2 of 2 answered</p>
      <svg class="chevron" width="22" height="48" viewBox="0 0 22 48" aria-hidden="true"><path d="M2 2 L20 24 L2 46" fill="none" stroke="#fff" stroke-width="2"/></svg>
    </li>
    <li class="topic">
      <svg class="dial" width="86" height="86" viewBox="0 0 86 86" aria-hidden="true">
        <circle cx="43" cy="43" r="40" fill="var(--dial-face)" stroke="#fff" stroke-width="3"/>
        <circle cx="43" cy="43" r="35" fill="none" stroke="var(--mint)" stroke-width="2"/>
        <path d="M43 43 L43 9 A34 34 0 0 1 63 15 Z" fill="var(--dial-track)"/>
        <circle cx="43" cy="43" r="26" fill="var(--dial-core)"/>
      </svg>
      <p class="name">Ethics</p>
      <p class="progress">2 of 2 answered</p>
      <svg class="chevron" width="22" height="48" viewBox="0 0 22 48" aria-hidden="true"><path d="M2 2 L20 24 L2 46" fill="none" stroke="#fff" stroke-width="2"/></svg>
    </li>
    <li class="topic">
      <svg class="dial" width="86" height="86" viewBox="0 0 86 86" aria-hidden="true">
        <circle cx="43" cy="43" r="40" fill="var(--dial-face)" stroke="#fff" stroke-width="3"/>
        <circle cx="43" cy="43" r="35" fill="none" stroke="var(--mint)" stroke-width="2"/>
        <path d="M43 43 L43 9 A34 34 0 0 1 63 15 Z" fill="var(--dial-track)"/>
        <circle cx="43" cy="43" r="26" fill="var(--dial-core)"/>
      </svg>
      <p class="name">Ethics</p>
      <p class="progress">2 of 2 answered</p>
      <svg class="chevron" width="22" height="48" viewBox="0 0 22 48" aria-hidden="true"><path d="M2 2 L20 24 L2 46" fill="none" stroke="#fff" stroke-width="2"/></svg>
    </li>
  </ul>
</body>
</html>
```